business card with logo

Would like a business card for an electrical contractor called BRANNOCK ELECTRICS.
No generic electrical imagery (light globe, powerpoints, ect). Would like a logo or symbol created in the design as part of the project . I would like crisp colour. No templated designs like Dorvex

is there any other designers willing to submit designs

Electrical

```html
<!DOCTYPE html>
<html lang="en">
<head>
<meta charset="utf-8">
<title>Brannock Electrics – Business Card</title>
<link rel="stylesheet" href="https://fonts.googleapis.com/css2?family=Roboto:wght@400;700&display=swap">
<style>
  :root {
    --bg: #ece7df;
    --card: #ffffff;
    --ink: #3d3d3f;
    --orange: #f0821e;
    --shadow: rgba(60, 40, 20, 0.18);
  }
  * { margin: 0; padding: 0; box-sizing: border-box; }
  html, body {
    width: 1200px;
    height: 1000px;
    overflow: hidden;
    background: var(--bg);
    font-family: "Roboto", Arial, sans-serif;
  }
  .stage {
    width: 1200px;
    height: 1000px;
    display: flex;
    flex-direction: column;
    align-items: center;
    justify-content: center;
    gap: 60px;
  }
  .card {
    width: 700px;
    height: 400px;
    background: var(--card);
    box-shadow: 0 10px 30px var(--shadow);
    position: relative;
  }
  .wordmark {
    display: flex;
    align-items: center;
    gap: 22px;
  }
  .wordmark__dot {
    flex: none;
    border-radius: 50%;
    background: var(--orange);
  }
  .wordmark__name {
    color: var(--ink);
    font-weight: 700;
    letter-spacing: 0.5px;
    white-space: nowrap;
  }

  /* Back of card: centred mark */
  .card--back {
    display: flex;
    align-items: center;
    justify-content: center;
  }
  .card--back .wordmark__dot { width: 78px; height: 78px; }
  .card--back .wordmark__name { font-size: 50px; }

  /* Front of card: mark and contact */
  .card--front { padding: 62px 60px; }
  .card--front .wordmark__dot { width: 60px; height: 60px; }
  .card--front .wordmark__name { font-size: 44px; }
  .contact {
    margin-top: 64px;
    padding-left: 82px;
  }
  .contact__name {
    color: var(--ink);
    font-size: 34px;
    font-weight: 400;
    line-height: 1.1;
  }
  .contact__licence {
    color: var(--orange);
    font-size: 24px;
    margin-top: 6px;
  }
  .contact__email {
    color: var(--ink);
    font-size: 22px;
    margin-top: 14px;
  }
  .contact__label { color: var(--orange); }
</style>
</head>
<body>
  <main class="stage">
    <section class="card card--back" aria-label="Card back">
      <div class="wordmark">
        <span class="wordmark__dot"></span>
        <span class="wordmark__name">BRANNOCK ELECTRICS</span>
      </div>
    </section>

    <section class="card card--front" aria-label="Card front">
      <div class="wordmark">
        <span class="wordmark__dot"></span>
        <span class="wordmark__name">BRANNOCK ELECTRICS</span>
      </div>
      <div class="contact">
        <p class="contact__name">Liam Brannock</p>
        <p class="contact__licence">REC # 48253</p>
        <p class="contact__email"><span class="contact__label">Email:</span> brannockelec@mailbox.com</p>
      </div>
    </section>
  </main>
</body>
</html>
```